Website Redesign for Pet Services Facility

We are looking to redesign our current website. The website must be designed in Wix so we can go in and easily edit throughout the life of the website. Design must be professional, simplistic and informative.

Our current website can be found at: www.plumhollowkennels.com

I would like the new site to be on one scrolling page. Sections to include:
Home page
Service teaser: Overnight Care, Grooming, Dog Daycare, Retail
An about us area with text on the left and a video on the right
Testimonial section
Overnight Section
Grooming Section
Dog Daycare Section
Retail
Meet the Team
Contact us: address, phone number, hours, etc.
Newsletter sign up and location map

A second page will be used for reservations and should include fields for.
Name, address, phone number, service: Overnight care, grooming, daycare, Arrival date, departure date, pet name, breed, special requests

Our phone number should be easily found through the pages. 'Request a Reservation' buttons should be found throughout page.

Text from our current site can be uesd as a filler for now as I will go in and finalize text when site is complete. Any photos can be used for now as I will go in and choose final photos as a later date.

I started playing with wix and started with a concept that I can share if you are interested, just let me know.

Industry/Entity Type

Pet

Number of Pages Required

2 page

Font styles to use
Sans Serif

Requirements
Must have
• 'Request a Reservation' Buttons
• Phone number easily visible
• location map
• Hours area
• Newsletter sign up

```html
<!DOCTYPE html>
<html lang="en">
<head>
<meta charset="utf-8">
<title>Plum Hollow – Services</title>
<link href="https://fonts.googleapis.com/css2?family=Roboto+Condensed:ital,wght@0,400;0,700;1,700&family=Dosis:wght@800&display=swap" rel="stylesheet">
<style>
  :root {
    --bg: #5a4a2f;
    --band-top: #231c12;
    --band-bottom: #4b3d27;
    --divider: #ffffff;
    --text: #f3efe6;
    --heading: #ffffff;
    --button: #a9dcdf;
    --button-text: #4b3b22;
    --photo-warm: #c98a3c;
    --photo-grass: #5f9a3a;
    --photo-blue: #3f86b8;
  }
  * { margin: 0; padding: 0; box-sizing: border-box; }
  html, body { width: 1200px; height: 900px; overflow: hidden; }
  body {
    position: relative;
    background: var(--bg);
    font-family: "Roboto Condensed", Arial, sans-serif;
    color: var(--text);
    font-size: 10.5px;
    line-height: 16px;
  }
  .abs { position: absolute; }
  .photo { position: absolute; }
  .divider { position: absolute; left: 0; width: 1200px; height: 10px; background: var(--divider); }
  .section-band {
    position: absolute; left: 0; width: 1200px; height: 52px;
    background: linear-gradient(to bottom, var(--band-top), var(--band-bottom));
    display: flex; align-items: center; justify-content: center;
  }
  .section-title {
    font-weight: 700; font-style: italic; font-size: 30px; letter-spacing: 0.5px;
    color: var(--heading); text-shadow: 2px 2px 3px rgba(0,0,0,0.7);
  }
  .subhead { font-weight: 700; font-size: 12px; color: var(--heading); }
  .bullets { list-style: none; }
  .bullets li::before { content: "•"; margin-right: 5px; }
  .bullets li { padding-left: 2px; }
  .btn {
    position: absolute; height: 38px; background: var(--button);
    border-radius: 3px; box-shadow: 0 2px 2px rgba(0,0,0,0.35);
    display: flex; align-items: center; justify-content: center; gap: 8px;
    font-family: "Dosis", "Arial Black", sans-serif; font-weight: 800;
    font-size: 17px; color: var(--button-text); letter-spacing: 0.3px;
  }
  .btn svg { width: 22px; height: 22px; }
  p + p { margin-top: 15px; }
</style>
</head>
<body>

<!-- Overnight care (continued) -->
<ul class="bullets abs" style="left:233px; top:-2px; width:420px;">
  <li style="list-style:none;">&nbsp;&nbsp;most discerning pup.</li>
  <li>Pets in the same family can stay together.</li>
  <li>Access to our full range of grooming services and spa packages</li>
  <li>Pick-up and Drop-off services available for busy dog owners.</li>
</ul>
<div class="photo" role="img" aria-label="Dog resting on a blue blanket" style="left:666px; top:0; width:327px; height:39px; background:linear-gradient(90deg, var(--photo-blue), #6aa8d6 40%, var(--photo-warm) 70%, #8a5a2a);"></div>

<div class="subhead abs" style="left:231px; top:81px;">Pricing</div>
<div class="abs" style="left:238px; top:100px; width:500px;">Overnight rates start at $35 per night. The cost of overnight care, however, will vary based on custom services.<br>Additional pets sharing the same suite receive a discounted rate.</div>
<div class="btn" style="left:850px; top:89px; width:142px;">GET STARTED
  <svg viewBox="0 0 24 24" aria-hidden="true"><g fill="currentColor"><ellipse cx="12" cy="16" rx="6" ry="5"/><ellipse cx="5" cy="10" rx="2.3" ry="3"/><ellipse cx="9.5" cy="5.5" rx="2.3" ry="3"/><ellipse cx="14.5" cy="5.5" rx="2.3" ry="3"/><ellipse cx="19" cy="10" rx="2.3" ry="3"/></g></svg>
</div>

<div class="divider" style="top:166px;"></div>

<!-- Grooming -->
<div class="section-band" style="top:176px;"><h2 class="section-title">GROOMING SERVICES</h2></div>

<div class="photo" role="img" aria-label="Golden retriever puppy lying on grass chewing a green toy" style="left:210px; top:240px; width:327px; height:228px; background:linear-gradient(135deg, var(--photo-grass) 0%, var(--photo-warm) 30%, #d99a4c 60%, #b06d2c 85%, var(--photo-grass) 100%);"></div>

<div class="abs" style="left:567px; top:238px; width:422px;">
  <p>Grooming at Plum Hollow is truly all about the client. From gentle massages, to deep coat condi-tioning, or moisturizing paw rubs we have our furry friend’s best interests in mind. Each grooming appointment can be custom tailored to the needs of the individual dogs and the requests of their owners.</p>
  <p>We understand that not every Golden Retriever gets trimmed the same way, just as not every Lab sheds as much as another. This is why we have developed a custom spa menu designed to pamper and soothe any guest. We use only all natural or organic products in our salon and have many options for dogs with sensitive skin or other allergies.</p>
  <p>Please take time to look through our complete spa menu to decide which services would best fit your dog. And feel free to contact us with any questions or to make an appointment.</p>
</div>
<div class="btn" style="left:825px; top:451px; width:168px;">GROOMING MENU
  <svg viewBox="0 0 24 24" aria-hidden="true"><g fill="currentColor"><ellipse cx="12" cy="16" rx="6" ry="5"/><ellipse cx="5" cy="10" rx="2.3" ry="3"/><ellipse cx="9.5" cy="5.5" rx="2.3" ry="3"/><ellipse cx="14.5" cy="5.5" rx="2.3" ry="3"/><ellipse cx="19" cy="10" rx="2.3" ry="3"/></g></svg>
</div>

<div class="divider" style="top:517px;"></div>

<!-- Daycare -->
<div class="section-band" style="top:527px;"><h2 class="section-title">DAYCARE</h2></div>

<div class="abs" style="left:231px; top:588px; width:426px;">
  <p>Socialization is one of the most important aspects of canine development. While staying at Plum Hollow your dog will play and socialize in a safe and supervised environment with other dogs of the same size or temperament. Here, dogs will have the chance to wrestle, fetch, run around or even catch an afternoon snooze in the warm summer sun. They will participate in play groups determined by their individual size and play style. Our climate controlled indoor play areas provide a comfortable space to romp around in and we use rubber flooring for a more cushioned play surface and to help prevent achy joints.</p>
</div>
<div class="subhead abs" style="left:231px; top:711px;">Benefits of Dog Daycare at Plum Hollow</div>
<ul class="bullets abs" style="left:233px; top:730px; width:420px;">
  <li>Provides physical activity, exercise and stimulation</li>
  <li>Increased social skills</li>
  <li>Decreased destructive behaviors due to boredom</li>
  <li>Builds confidence in timid or fearful dogs</li>
  <li>Offers a safe and controlled environment for appropriate play</li>
</ul>

<div class="photo" role="img" aria-label="Two puppies playing on grass in a fenced yard" style="left:666px; top:590px; width:327px; height:229px; background:linear-gradient(to bottom, #b9bcb3 0%, #9ea39a 40%, #7d6a55 58%, var(--photo-grass) 72%, #4f8a2e 100%);"></div>

<div class="subhead abs" style="left:231px; top:827px;">Pricing</div>
<div class="abs" style="left:238px; top:846px; width:470px;">Daycare is available any day during our regular business hours. We offer half days for up to five hours of play starting at $14.25 and full days of play starting at $19.25.</div>
<div class="btn" style="left:850px; top:850px; width:142px;">GET STARTED
  <svg viewBox="0 0 24 24" aria-hidden="true"><g fill="currentColor"><ellipse cx="12" cy="16" rx="6" ry="5"/><ellipse cx="5" cy="10" rx="2.3" ry="3"/><ellipse cx="9.5" cy="5.5" rx="2.3" ry="3"/><ellipse cx="14.5" cy="5.5" rx="2.3" ry="3"/><ellipse cx="19" cy="10" rx="2.3" ry="3"/></g></svg>
</div>

</body>
</html>
```